Meridale Cleaning Services

In need of a business card design suited for a growing cleaning company.

We offer our cleaning and maintenance services to a wide range of clients including but not limited to the following: constuction industry, hospitality, commercial, industrial and domestic

I want the card to be very noticable, i would like people to say 'hey, great card!' when i hand them my card.double sided would be nice

we want our business to come across as exceedingly professional and innovative (different).

a contemporary design is what we have in mind
we want to present an image of a quality business with a high standard of excellence in consistent service.

i just really need a card that persuades top end quality,
our business is very certified and also strives towards environmentaly friendly alternatives
Updates

hey sorry, i have uploaded my company logo design and name
cheers.

hey guys i have added my company logo/name file on my brief page. many thanks

sorry guys a typo in the brief..
address is Tolley Rd. not Tolly Rd
thanks

Industry/Entity Type

Industrial

Requirements
Must have
• company name: meridale cleaning services
operations manager: Colm Varetti
Tel: (02)9373 6204
Fax: (02)8645 7712
Mob: 0438571490

address: 47 Tolly RD Pymble NSW 2073
Postal Adress: PO Box 5832 North Ryde NSW 2113
email: meridaleclean@wexanet.com.au
website: meridalecleaningservices.com.au

```html
<!DOCTYPE html>
<html lang="en">
<head>
<meta charset="utf-8">
<title>Meridale Cleaning Services – Business Card</title>
<link href="https://fonts.googleapis.com/css2?family=Open+Sans:wght@600&family=Arimo:wght@400;700&display=swap" rel="stylesheet">
<style>
  :root {
    --brand-blue: #1f6fbf;
    --text-blue: #1b63b8;
    --text-green: #3d8a2c;
    --green-light: #d9ebb4;
    --green-mid: #bcd98c;
    --green-deep: #a8c97a;
    --blue-light: #a9c9ec;
    --blue-mid: #8fa9dc;
    --blue-deep: #7f9bd6;
    --mark-fill: #3f93d6;
    --divider: #111111;
    --paper: #ffffff;
  }
  * { margin: 0; padding: 0; box-sizing: border-box; }
  html, body { width: 998px; height: 1200px; overflow: hidden; background: var(--paper); }
  .sheet { position: relative; width: 998px; height: 1200px; }
  .card { position: absolute; left: 0; width: 998px; height: 597px; overflow: hidden; background: var(--paper); }
  .card--front { top: 0; }
  .card--back { top: 600px; height: 600px; }
  .divider { position: absolute; left: 0; top: 596px; width: 998px; height: 4px; background: var(--divider); }
  .waves { position: absolute; inset: 0; width: 100%; height: 100%; }
  .brand-dot { position: absolute; border-radius: 50%; background: var(--mark-fill); }
  .brand-name {
    position: absolute; font-family: "Open Sans", Arial, sans-serif; font-weight: 600;
    color: var(--brand-blue); text-align: center; line-height: 1;
  }
  .brand-name .word { display: block; }
  .front-name { left: 0; width: 998px; top: 420px; }
  .front-name .word--main { font-size: 96px; letter-spacing: -1px; }
  .front-name .word--sub { font-size: 36px; margin-top: 12px; letter-spacing: 1px; }
  .back-name { left: 322px; top: 55px; text-align: left; }
  .back-name .word--main { font-size: 70px; letter-spacing: -1px; }
  .back-name .word--sub { font-size: 27px; margin-top: 8px; letter-spacing: 1px; }
  .contact { position: absolute; left: 0; width: 998px; text-align: center; font-family: Arimo, Arial, sans-serif; }
  .contact--phones { top: 260px; color: var(--text-blue); }
  .role { font-size: 28px; line-height: 32px; }
  .person { font-size: 37px; font-weight: 700; line-height: 42px; }
  .phone { font-size: 26px; line-height: 34px; }
  .contact--details { top: 430px; color: var(--text-green); }
  .detail { font-size: 21px; line-height: 35px; }
</style>
</head>
<body>
<div class="sheet">
  <section class="card card--front">
    <svg class="waves" viewBox="0 0 998 597" preserveAspectRatio="none" aria-hidden="true">
      <path d="M0 0 H60 C120 150 230 300 215 420 C205 500 185 560 180 597 H0 Z" fill="var(--green-light)"/>
      <path d="M0 60 C80 200 140 330 120 450 C110 520 100 570 95 597 H0 Z" fill="var(--green-mid)"/>
      <path d="M720 0 H998 V597 H890 C880 500 860 380 850 300 C835 180 760 90 720 0 Z" fill="var(--blue-light)"/>
      <path d="M800 0 H998 V597 H935 C930 470 915 350 900 250 C885 150 840 80 800 0 Z" fill="var(--blue-mid)"/>
    </svg>
    <div class="brand-dot" style="left:355px;top:60px;width:270px;height:270px;"></div>
    <div class="brand-name front-name">
      <span class="word word--main">Meridale</span>
      <span class="word word--sub">CLEANING SERVICES</span>
    </div>
  </section>

  <div class="divider"></div>

  <section class="card card--back">
    <svg class="waves" viewBox="0 0 998 600" preserveAspectRatio="none" aria-hidden="true">
      <path d="M0 0 H55 C110 140 205 300 195 420 C190 500 180 560 178 600 H0 Z" fill="var(--green-light)"/>
      <path d="M0 60 C70 200 130 330 115 450 C108 520 100 570 98 600 H0 Z" fill="var(--green-mid)"/>
      <path d="M735 0 H998 V600 H885 C878 500 862 380 850 300 C835 180 770 90 735 0 Z" fill="var(--blue-light)"/>
      <path d="M810 0 H998 V600 H935 C930 470 915 350 902 250 C888 150 845 80 810 0 Z" fill="var(--blue-mid)"/>
    </svg>
    <div class="brand-dot" style="left:150px;top:42px;width:150px;height:150px;"></div>
    <div class="brand-name back-name">
      <span class="word word--main">Meridale</span>
      <span class="word word--sub">CLEANING SERVICES</span>
    </div>
    <div class="contact contact--phones">
      <p class="role">OPERATIONS MANAGER:</p>
      <p class="person">COLM VARETTI</p>
      <p class="phone">TEL: (02)9373 6204</p>
      <p class="phone">FAX: (02)8645 7712</p>
      <p class="phone">MOB: 0438571490</p>
    </div>
    <div class="contact contact--details">
      <p class="detail">Address: 47 Tolley RD Pymble NSW 2073</p>
      <p class="detail">Postal Adress: PO Box 5832 North Ryde NSW 2113</p>
      <p class="detail">Email: meridaleclean@wexanet.com.au</p>
      <p class="detail">Website: meridalecleaningservices.com.au</p>
    </div>
  </section>
</div>
</body>
</html>
```